Wesbite design for Investment Firm

We want a basic (clean) website that follows the form, fonts and colors of our attachments. This is for a financial investment management firm, but we have a boutique (anti-Wall Street) approach. Site should have an Home Page (Logo up top - room for basic copy on bottom, Philosophy Page (room for Quarterly Letter attachment and basic copy, Performance Page (room for Performance Overview and Performance Analysis and basic copy), Team Page, Commentary Page and Contact
Updates

Reason: Some designers have asked for an extension. Again, please only use image of Train Station or Train Station Logo in design.

Target Market(s)

Small and mid-size financial advisors from across the country

Industry/Entity Type

Financial

Number of Pages Required

5+ page

Font styles to use
Other font styles liked:
• Palotino Linotype

Colors
3176b5
cfdeed
ffffff

Requirements
Must have
• Please refer to existing site www.qarvelton.com. Of note, this is too complex / cluttered. We simply want Blur, Grey and White consistent with attachments. The copy is pretty good, but will be simplified (and no quotes)
Should not have
• No images other than train station logo and / or train station image

```html
<!DOCTYPE html>
<html lang="en">
<head>
<meta charset="utf-8">
<title>Harlow Bridge Investment Company</title>
<link rel="stylesheet" href="https://fonts.googleapis.com/css2?family=EB+Garamond:wght@400;500;600&family=Crimson+Pro:ital,wght@0,400;0,600;0,700;1,400&family=Open+Sans:wght@400;600&display=swap">
<style>
:root{
  --blue:#3176b5;
  --blue-dark:#1f4f8a;
  --navy:#14217a;
  --pale:#cfdeed;
  --white:#ffffff;
  --grey-bg:#f5f5f5;
  --text:#222222;
  --gold:#8f6508;
  --gold-text:#8a6d1c;
  --muted:#9a9a9a;
  --rule:#dddddd;
  --black:#0d0d0d;
}
*{margin:0;padding:0;box-sizing:border-box}
html,body{width:1200px;height:2689px;overflow:hidden}
body{background:var(--white);font-family:"Crimson Pro",serif;color:var(--text);position:relative}
.serif-caps{font-family:"EB Garamond",serif;font-variant:small-caps;letter-spacing:1px;font-weight:600;color:var(--blue-dark)}

/* top bar */
.topbar{height:43px;background:var(--blue);display:flex;align-items:center;padding:0 100px 0 108px;color:var(--white);font-family:"Open Sans",sans-serif;font-size:12.5px}
.social-squares{display:flex;gap:8px}
.social-squares span{width:22px;height:22px;border:1px solid rgba(255,255,255,.8);display:block}
.topbar .info{margin-left:auto;display:flex;gap:110px}
.topbar b{font-weight:600}

/* brand */
.brand{text-align:center;padding-top:35px;height:192px}
.brand h1{font-family:"EB Garamond",serif;font-weight:500;font-size:42px;color:var(--navy);line-height:1}
.brand p{font-family:"EB Garamond",serif;font-size:19px;color:var(--gold-text);margin-top:6px}

/* nav */
.nav{position:absolute;top:192px;left:84px;width:1021px;height:42px;background:var(--pale);display:flex;align-items:center;font-family:"Open Sans",sans-serif;font-size:13.5px}
.nav a{color:var(--blue);text-decoration:none;margin-left:24px;margin-right:30px}
.nav .letter{margin-left:auto;margin-right:0;height:42px;background:var(--gold);color:var(--white);display:flex;align-items:center;padding:0 20px;font-family:"Crimson Pro",serif;font-weight:700;font-size:13.5px;letter-spacing:.3px;text-transform:uppercase}

/* hero */
.hero{position:absolute;top:235px;left:84px;width:1021px;height:448px;overflow:hidden}
.hero-photo{position:absolute;inset:0;background:linear-gradient(180deg,#5a6478 0%,#6e6a66 30%,#8d8d8f 55%,#5e5e60 100%)}
.hero-copy{position:absolute;top:195px;width:100%;text-align:center;color:var(--white);font-family:"EB Garamond",serif}
.hero-copy .l1{font-size:33px;letter-spacing:1px}
.hero-copy .l2{font-size:37px;font-weight:600;letter-spacing:.5px;margin-top:2px}
.hero-btns{position:absolute;top:316px;width:100%;display:flex;justify-content:center;gap:8px;font-family:"Open Sans",sans-serif;font-size:13px}
.hero-btns span{height:40px;display:flex;align-items:center;padding:0 25px}
.btn-blue{background:var(--blue);color:var(--white)}
.btn-pale{background:var(--pale);color:var(--blue-dark)}
.arrow{position:absolute;top:208px;width:34px;height:32px;display:flex;align-items:center;justify-content:center}
.arrow.left{left:23px;background:#9aa2ad}
.arrow.right{right:26px;background:var(--blue)}
.dots{position:absolute;top:399px;width:100%;display:flex;justify-content:center;gap:7px}
.dots i{width:20px;height:3px;background:rgba(255,255,255,.6)}
.dots i:first-child{background:var(--white)}

/* section headings */
.sec-title{text-align:center;font-size:31px}
.sec-title::after{content:"";display:block;width:70px;height:2px;background:var(--blue);margin:10px auto 0}

/* welcome */
.welcome{position:absolute;top:705px;left:0;width:1200px;height:353px}
.welcome-art{position:absolute;left:300px;top:20px;width:600px;height:320px;border-radius:50%;background:radial-gradient(ellipse at center,rgba(49,118,181,.10) 0%,rgba(49,118,181,.05) 45%,rgba(255,255,255,0) 72%)}
.welcome .sec-title{position:relative;padding-top:10px}
.copy{position:relative;text-align:center;font-size:15.5px;line-height:22px;width:1030px;margin:0 auto}
.copy p+p{margin-top:20px}
.welcome .copy{margin-top:25px}
.read-more{position:absolute;top:263px;left:502px;width:181px;height:40px;background:#5e93c8;color:var(--white);font-family:"Open Sans",sans-serif;font-size:13px;display:flex;align-items:center;justify-content:center}

/* strategy */
.strategy{position:absolute;top:1058px;left:0;width:1200px;height:323px;background:var(--grey-bg)}
.strategy .sec-title{padding-top:30px}
.strategy .copy{margin-top:36px}

/* partners */
.partners{position:absolute;top:1381px;left:0;width:1200px;height:475px}
.partners .kicker{text-align:center;font-style:italic;color:var(--blue-dark);font-size:17px;padding-top:22px}
.partners .sec-title{margin-top:2px}
.partners .sec-title::after{display:none}
.logo-grid{position:absolute;top:165px;left:95px;width:995px;display:grid;grid-template-columns:repeat(4,1fr)}
.logo-cell{height:118px;display:flex;align-items:center;justify-content:center;gap:10px;font-family:"Crimson Pro",serif;font-weight:600;font-size:24px;color:var(--muted);border-right:1px solid var(--rule);border-bottom:1px solid var(--rule)}
.logo-cell:nth-child(4n){border-right:none}
.logo-cell:nth-child(n+5){border-bottom:none;margin-top:14px;height:106px}
.logo-cell i{width:14px;height:14px;border-radius:50%;background:var(--muted);display:block}

/* commentary */
.lower{position:absolute;top:1856px;left:0;width:1200px;height:493px;background:var(--grey-bg)}
.col-left{position:absolute;left:95px;top:36px;width:470px}
.col-right{position:absolute;left:626px;top:36px;width:465px}
.col-title{font-size:26px}
.post{margin-top:26px}
.post:first-of-type{margin-top:22px}
.post h3{font-family:"Open Sans",sans-serif;font-size:13.5px;font-weight:600;color:var(--blue);text-transform:uppercase}
.post .date{font-family:"Crimson Pro",serif;font-weight:700;font-size:12px;margin-top:4px}
.post p{font-size:15.5px;line-height:19.5px;margin-top:12px}
.post .cta{display:inline-block;margin-top:12px;background:var(--gold);color:var(--white);font-family:"Open Sans",sans-serif;font-weight:600;font-size:11.5px;padding:9px 16px;text-transform:uppercase}
.testimonial{position:absolute;top:59px;left:0;width:465px;height:341px;background:#e9f0f8;border:1px solid #93b3d6;text-align:center}
.quote-mark{position:absolute;font-family:"EB Garamond",serif;font-size:48px;color:#aab3bf;line-height:1}
.quote-mark.open{left:18px;top:52px}
.quote-mark.close{right:96px;top:136px}
.testimonial blockquote{font-size:15.5px;line-height:20px;padding:72px 34px 0}
.avatar{width:62px;height:62px;border-radius:50%;background:linear-gradient(160deg,#c9a98f,#6a4c3c);margin:40px auto 0}
.testimonial .name{font-family:"Open Sans",sans-serif;font-weight:600;font-size:12px;color:var(--blue);margin-top:10px}
.t-dots{display:flex;justify-content:center;gap:6px;margin-top:16px}
.t-dots i{width:28px;height:5px;border-radius:3px;background:var(--black)}
.t-dots i:first-child{background:var(--gold)}

/* footer */
.footer{position:absolute;top:2349px;left:0;width:1200px;height:273px;background:var(--blue);color:var(--white)}
.f-col{position:absolute;top:35px}
.f-col h4{font-family:"Open Sans",sans-serif;font-weight:600;font-size:12.5px;letter-spacing:.6px;text-transform:uppercase}
.f-links{left:100px;width:232px}
.f-links ul{list-style:none;margin-top:18px}
.f-links li{font-size:13.5px;padding:8px 0 13px 20px;border-bottom:1px solid rgba(255,255,255,.5);position:relative}
.f-links li::before{content:"»";position:absolute;left:4px;top:6px}
.f-contact{left:420px;width:240px}
.f-contact .row{display:flex;gap:14px;font-size:13.5px;line-height:19px;margin-top:20px}
.f-contact .row svg{flex:none;margin-top:3px}
.f-about{left:685px;width:400px}
.f-about p{font-size:14px;line-height:20px;margin-top:18px;color:#e3ecf6}
.f-brand{text-align:center;margin-top:26px;width:370px}
.f-brand .n{font-family:"EB Garamond",serif;font-size:24px;color:#dbe6f2;white-space:nowrap;line-height:1.1}
.f-brand .s{font-family:"EB Garamond",serif;font-size:13px;color:#8fc3ee;margin-top:2px}

/* bottom bar */
.bottom{position:absolute;top:2622px;left:0;width:1200px;height:67px;background:var(--black);color:var(--white);display:flex;align-items:center;padding:0 100px;font-family:"Open Sans",sans-serif;font-size:12.5px}
.legal{margin-left:115px;color:#3a8ee0}
.legal span{margin:0 6px;color:#3a8ee0}
.connect{margin-left:auto;display:flex;align-items:center;gap:8px}
.connect .c{width:30px;height:30px;border-radius:50%;display:block}
</style>
</head>
<body>

<header class="topbar">
  <div class="social-squares"><span></span><span></span><span></span><span></span><span></span></div>
  <div class="info">
    <div><b>Opening Hour:</b> Mon-sat 8:00-21:00</div>
    <div><b>Phone:</b> 555.018.4420</div>
    <div><b>Email:</b> info@hbic-mail.com</div>
  </div>
</header>

<div class="brand">
  <h1>Harlow Bridge Investment Company</h1>
  <p>Separately Managed Accounts</p>
</div>

<nav class="nav">
  <a>Home</a><a>Philosophy</a><a>Performance</a><a>Team</a><a>Commentary</a><a>Contact</a>
  <span class="letter">Download&nbsp; Investment Adviser's Letter</span>
</nav>

<section class="hero">
  <div class="hero-photo" role="img" aria-label="Photograph of the historic wooden train station building"></div>
  <div class="arrow left"><svg width="16" height="10" viewBox="0 0 16 10"><path d="M15 5H2M6 1L2 5l4 4" stroke="#fff" stroke-width="1.8" fill="none"/></svg></div>
  <div class="arrow right"><svg width="16" height="10" viewBox="0 0 16 10"><path d="M1 5h13M10 1l4 4-4 4" stroke="#fff" stroke-width="1.8" fill="none"/></svg></div>
  <div class="hero-copy">
    <div class="l1">MANAGE ASSETS FOR BOTH</div>
    <div class="l2">INDIVIDUALS AND INSTITUTIONS</div>
  </div>
  <div class="hero-btns"><span class="btn-blue">EXPLORE OUR SERVICES</span><span class="btn-pale">READ MORE ABOUT US</span></div>
  <div class="dots"><i></i><i></i><i></i></div>
</section>

<section class="welcome">
  <div class="welcome-art" role="img" aria-label="Faint drawing of the train station"></div>
  <h2 class="sec-title serif-caps">Welcome To Harlow Bridge Investment</h2>
  <div class="copy">
    <p>At Harlow Bridge, we employ an <b>absolute return mindset to long-only value investing.</b>&nbsp; As fundamentally focused equity investors, we seek to identify good business models with high barriers to entry trading at substantial discounts to our conservative estimate of fair value.&nbsp; Finally, we contend that <b>entry price is a significant determinant of return.</b></p>
    <p>We ignore Wall Street research and our approach is not constrained by market size.&nbsp; Our <b>independence, patience</b> and <b>clearly defined process</b> drive the investment returns we seek for ourselves and our clients.</p>
  </div>
  <div class="read-more">READ MORE</div>
</section>

<section class="strategy">
  <h2 class="sec-title serif-caps">Investment Strategy</h2>
  <div class="copy">
    <p>At the core of our approach is the fundamental belief that the <b>price we pay for an investment determines the return.</b>&nbsp; Further, trying to keep pace with the market in all environments likely promotes poor decisions and increases the probability of losses.&nbsp; By focusing on the Harlow Bridge process, positive outcomes over complete market cycles emerge.</p>
    <p>Importantly, buying an asset at fair value will only generate an average return.&nbsp; By contrast, we invest in proven businesses trading at a discount.&nbsp; As fair value is a moving target subject to&nbsp; uncontrollable variables, we deploy capital only when a margin of safety offers us sufficient protection and investment return potential.</p>
  </div>
</section>

<section class="partners">
  <div class="kicker">awesome clients</div>
  <h2 class="sec-title serif-caps">Our Partners</h2>
  <div class="logo-grid">
    <div class="logo-cell">Tandry</div>
    <div class="logo-cell"><i></i>Mossfield</div>
    <div class="logo-cell">Corvane</div>
    <div class="logo-cell">Lindqvist</div>
    <div class="logo-cell"><i></i>Orrelle</div>
    <div class="logo-cell">Bramhill</div>
    <div class="logo-cell"><i></i>Castavo</div>
    <div class="logo-cell">Wexmoor</div>
  </div>
</section>

<section class="lower">
  <div class="col-left">
    <h2 class="col-title serif-caps">Latest Commentary</h2>
    <article class="post">
      <h3>Core Equity Portfolio – Q2 2017</h3>
      <div class="date">August 10, 2017</div>
      <p>Based on our estimate of fair value relative to the company’s current stock price, we determine each company’s current margin of safety in the Core Equity ...</p>
      <span class="cta">Continue Reading</span>
    </article>
    <article class="post">
      <h3>Core Equity Portfolio – Q2 2017</h3>
      <div class="date">August 10, 2017</div>
      <p>Based on our estimate of fair value relative to the company’s current stock price, we determine each company’s current margin of safety in the Core Equity ...</p>
      <span class="cta">Continue Reading</span>
    </article>
  </div>
  <div class="col-right">
    <h2 class="col-title serif-caps">What Client’s Says?</h2>
    <div class="testimonial">
      <span class="quote-mark open">“</span>
      <span class="quote-mark close">”</span>
      <blockquote>These days are all share them with me oh baby said inspect Califomy till the one day when the lady they knew escaped from maximum security stockade.</blockquote>
      <div class="avatar" role="img" aria-label="Client portrait"></div>
      <div class="name">NORA ELLIS</div>
      <div class="t-dots"><i></i><i></i><i></i></div>
    </div>
  </div>
</section>

<footer class="footer">
  <div class="f-col f-links">
    <h4>Quick Links</h4>
    <ul>
      <li>Performance Overview</li>
      <li>Performance Analysis</li>
      <li>Verification Statement</li>
      <li>Harlow Bridge ADV Part 2</li>
    </ul>
  </div>
  <div class="f-col f-contact">
    <h4>Contact Us</h4>
    <div class="row"><svg width="10" height="14" viewBox="0 0 10 14"><path d="M5 0a5 5 0 0 0-5 5c0 4 5 9 5 9s5-5 5-9a5 5 0 0 0-5-5zm0 7a2 2 0 1 1 0-4 2 2 0 0 1 0 4z" fill="#fff"/></svg><div>4120 Elm Crest Avenue,<br>Suite 1200<br>Fairbrook, OH 43122</div></div>
    <div class="row"><svg width="12" height="12" viewBox="0 0 12 12"><path d="M2.5 0.5l2 2.5-1 1.5c.8 1.6 1.9 2.7 3.5 3.5l1.5-1 2.5 2-1 2.5C5 11.5.5 7 .5 1.5z" fill="#fff"/></svg><div>555.018.4420</div></div>
    <div class="row"><svg width="13" height="10" viewBox="0 0 13 10"><rect x="0" y="0" width="13" height="10" rx="1" fill="#fff"/><path d="M0.5 0.8l6 4.7 6-4.7" stroke="#3176b5" stroke-width="1.2" fill="none"/></svg><div>info@hbic-mail.com</div></div>
  </div>
  <div class="f-col f-about">
    <h4>About Harlow Bridge Investment</h4>
    <p>Aliquam sit amet ipsum eu tellus tincidunt commodo. Aenean metus tellus, vehicula at nisl vel, laoreet gravida risus. Integer nec fringilla neque. Vivamus tincidunt dui vitae augue. Aliquam sit amet ipsum eu tellus tincidunt commodo.</p>
    <div class="f-brand">
      <div class="n">Harlow Bridge Investment Company</div>
      <div class="s">Separately Managed Accounts</div>
    </div>
  </div>
</footer>

<div class="bottom">
  <div>© 21017, All Rights Reserved</div>
  <div class="legal">Worldwide<span>|</span>Privacy Policy<span>|</span>Terms &amp; Use<span>|</span>US trademarks</div>
  <div class="connect">
    <span>Connect With Us:</span>
    <i class="c" style="background:#3b5998"></i>
    <i class="c" style="background:#1da1f2"></i>
    <i class="c" style="background:#0e76a8"></i>
    <i class="c" style="background:#3176b5"></i>
    <i class="c" style="background:#d0202a"></i>
  </div>
</div>

</body>
</html>
```